Clone https://dunmerio.com (fully functional wordpress site with wooCommerce)

1) Clone or recreate the site in WordPress Woocomerece
2) Connect to our existing plovex account.
3) Make our text only changes (not style changes or anything complex.

We will provide all graphics and content to be copied and pasted in place of the existing text / graphics.

Please do not submit a design only. Thanks in advance.

Target Market(s)

Wordpress developer

Number of Pages Required

5+ page

Font styles to use
Sans Serif

Colors
acd036
9bcb3c
cadf82
eaf2ce

Requirements
Must have
• Fully functional wordpress site with Woo Comerece pluged in.
Should not have
• Design only

```html
<!DOCTYPE html>
<html lang="en">
<head>
<meta charset="utf-8">
<title>Dunmerio — 24/7 Live Answering Service</title>
<link href="https://fonts.googleapis.com/css2?family=Lato:wght@300;400;700&family=Open+Sans:wght@400;600;700&display=swap" rel="stylesheet">
<style>
:root{
  --green:#8cc63f;
  --green-deep:#6fa82d;
  --lime:#cadf82;
  --lime-pale:#eaf2ce;
  --olive:#7a9a4f;
  --footer:#3f6e1f;
  --footer-bar:#2b4417;
  --ink:#333;
  --ink-soft:#666;
  --rule:#c9c9c9;
  --white:#fff;
  --blue:#1d8fd0;
  --blue-pale:#d6ebf7;
}
*{box-sizing:border-box;margin:0;padding:0}
html,body{width:1200px;height:4270px;overflow:hidden}
body{font-family:"Open Sans",Arial,sans-serif;color:var(--ink);background:var(--white);position:relative}
section,header,footer{position:absolute;left:0;width:1200px}

/* hero */
.hero{top:0;height:565px}
.hero-photo{position:absolute;inset:0;background:radial-gradient(ellipse at 72% 40%,#6a6258 0%,#3b3a36 38%,#1f1f1f 80%)}
.nav{position:absolute;top:30px;left:0;width:1200px;height:40px}
.brand{position:absolute;left:130px;top:6px;display:flex;align-items:center;gap:10px;color:var(--white);font-family:"Lato",sans-serif;font-weight:700;font-size:18px}
.brand-dot{width:22px;height:22px;border-radius:50%;background:var(--green)}
.nav-links{position:absolute;left:466px;top:8px;display:flex;gap:22px;list-style:none;font-size:15px;color:var(--white)}
.nav-links .active{color:var(--green)}
.nav-search{position:absolute;left:1062px;top:10px}
.hero-title{position:absolute;top:268px;width:100%;text-align:center;color:var(--white);font-family:"Lato",sans-serif;font-weight:400;font-size:27px}

/* shared headings */
.rule-heading{position:absolute;left:120px;width:960px;display:flex;align-items:center;gap:30px;font-family:"Lato",sans-serif;font-weight:300;font-size:23px;color:var(--olive);white-space:nowrap}
.rule-heading::before,.rule-heading::after{content:"";flex:1;height:1px;background:var(--rule)}

/* team */
.team{top:565px;height:500px}
.team .rule-heading{top:70px}
.agents{position:absolute;top:155px;left:120px;width:960px;display:flex;justify-content:space-between}
.agent{width:270px;text-align:center}
.avatar{width:125px;height:125px;border-radius:50%;margin:0 auto;background:radial-gradient(circle at 50% 40%,#b89a86,#6d5a4f 60%,#ddd 62%);border:3px solid #eee}
.agent-name{margin-top:25px;font-size:15px;color:#222}
.agent-role{font-size:12px;font-weight:700;color:#222;margin-top:4px}
.agent-quote{margin-top:18px;font-size:13px;line-height:1.55;color:var(--ink-soft)}

/* services */
.services{top:1065px;height:840px;background:linear-gradient(90deg,#e6e6e6 0%,#fff 18%,#fff 82%,#e6e6e6 100%)}
.services .rule-heading{top:70px}
.feature{position:absolute;width:290px;text-align:center}
.feature svg{display:block;margin:0 auto 6px}
.feature h3{font-weight:400;font-size:15px;color:#222}
.feature p{font-size:11.5px;line-height:1.45;color:var(--ink-soft);margin-top:3px}
.phone-photo{position:absolute;left:455px;top:400px;width:275px;height:418px;background:linear-gradient(180deg,#f3f3f3 0%,#d9d9d9 45%,#e4d3c6 100%)}
.cta{position:absolute;left:418px;top:818px;width:366px;height:44px;background:var(--green-deep);color:var(--white);font-size:16px;display:flex;align-items:center;justify-content:center;z-index:2}

/* languages */
.languages{top:1905px;height:500px}
.lang{position:absolute;top:92px;width:275px}
.lang h2{font-family:"Lato",sans-serif;font-weight:700;font-size:32px;color:#222}
.lang h3{font-family:"Lato",sans-serif;font-weight:400;font-size:23px;color:var(--green);margin:22px 0 26px}
.lang p{font-size:12px;line-height:1.6;color:var(--ink-soft)}
.greeting-art{position:absolute;left:497px;top:197px;width:210px;height:125px;background:radial-gradient(ellipse at center,var(--blue-pale) 0%,#fff 75%)}
.languages .rule-heading{top:555px}

/* testimonial */
.testimonial{top:2605px;height:365px;background:var(--lime)}
.tabs-card{position:absolute;left:120px;top:72px;width:960px;height:220px;background:var(--white);border:1px solid #ddd}
.tab-row{display:flex;background:#f1f1f1;height:30px}
.tab{width:150px;font-size:11px;display:flex;align-items:center;justify-content:center;color:#444;border-right:1px solid #ddd}
.tab.current{background:var(--white)}
.client-photo{position:absolute;left:36px;top:58px;width:100px;height:100px;border-radius:50%;background:radial-gradient(circle at 50% 40%,#5b4236,#2d221d 60%,#e5e5e5 62%)}
.tab-text{position:absolute;left:262px;top:54px;width:660px;font-size:12.5px;line-height:1.85;color:#444}

/* stats */
.stats{top:2970px;height:305px}
.stat{position:absolute;top:75px;width:290px}
.stat h3{font-family:"Lato",sans-serif;font-weight:400;font-size:22px;color:#222}
.stat-body{display:flex;align-items:flex-end;gap:10px;margin-top:26px}
.stat-num{font-family:"Lato",sans-serif;font-weight:300;font-size:68px;line-height:.8;color:#333}
.stat-body p{font-size:12px;line-height:1.5;color:var(--ink-soft)}

/* demo */
.demo{top:3275px;height:685px;background:linear-gradient(180deg,#8aa868,#7c9a5a)}
.demo h2{position:absolute;top:95px;width:100%;text-align:center;font-family:"Lato",sans-serif;font-weight:400;font-size:28px;color:var(--white)}
.field{position:absolute;left:122px;width:958px;height:42px;background:rgba(255,255,255,.88);font-size:11px;color:#999;padding:13px 14px}
.field.message{height:126px}
.captcha-label{position:absolute;left:876px;top:599px;font-size:11px;color:#eee}
.captcha-box{position:absolute;left:920px;top:583px;width:48px;height:44px;background:var(--white)}
.submit{position:absolute;left:978px;top:583px;width:102px;height:44px;border:2px solid var(--blue);color:var(--white);font-size:13px;display:flex;align-items:center;justify-content:center}

/* footer */
.site-footer{top:3960px;height:268px;background:var(--footer)}
.footer-art{position:absolute;left:120px;top:45px;width:215px;height:185px;border-radius:8px;background:radial-gradient(circle,#4b87a9 0%,rgba(63,110,31,0) 70%)}
.footer-links{position:absolute;top:62px;list-style:none;font-size:13px;line-height:2.1;color:var(--white)}
.footer-links li::before{content:"• "}
.footer-bar{top:4228px;height:42px;background:var(--footer-bar);color:#ddd;font-size:11.5px}
.footer-bar .legal{position:absolute;left:122px;top:14px}
.footer-bar b{color:var(--white)}
.social{position:absolute;right:120px;top:14px;display:flex;gap:18px}
.social span{width:13px;height:13px;border-radius:50%;background:#ddd}
</style>
</head>
<body>

<header class="hero">
  <div class="hero-photo" role="img" aria-label="Smiling call agent wearing a headset microphone"></div>
  <nav class="nav">
    <div class="brand"><span class="brand-dot"></span>Dunmerio</div>
    <ul class="nav-links">
      <li class="active">Home</li><li>Services</li><li>Customers</li><li>Pricing</li><li>Contact Us</li><li>Login</li><li>Free Trial</li>
    </ul>
    <svg class="nav-search" width="16" height="16" viewBox="0 0 16 16"><circle cx="6.5" cy="6.5" r="5" fill="none" stroke="#fff" stroke-width="1.8"/><line x1="10.2" y1="10.2" x2="15" y2="15" stroke="#fff" stroke-width="1.8"/></svg>
  </nav>
  <h1 class="hero-title">24/7 Live Answering Service</h1>
</header>

<section class="team">
  <h2 class="rule-heading">Inbound call handling from agents that wow</h2>
  <div class="agents">
    <div class="agent"><div class="avatar" role="img" aria-label="Portrait of team lead"></div><div class="agent-name">Marla Kensit</div><div class="agent-role">Team lead</div><p class="agent-quote">"I take pride in my job! By answering the phone with a smile, I'm giving callers wow-level service they really appreciate."</p></div>
    <div class="agent"><div class="avatar" role="img" aria-label="Portrait of team lead"></div><div class="agent-name">Marla Kensit</div><div class="agent-role">Team lead</div><p class="agent-quote">"I take pride in my job! By answering the phone with a smile, I'm giving callers wow-level service they really appreciate."</p></div>
    <div class="agent"><div class="avatar" role="img" aria-label="Portrait of team lead"></div><div class="agent-name">Marla Kensit</div><div class="agent-role">Team lead</div><p class="agent-quote">"I take pride in my job! By answering the phone with a smile, I'm giving callers wow-level service they really appreciate."</p></div>
  </div>
</section>

<section class="services">
  <h2 class="rule-heading">A lot more than just message taking</h2>

  <div class="feature" style="left:110px;top:150px"><svg width="40" height="36" viewBox="0 0 40 36"><rect x="3" y="3" width="34" height="24" fill="none" stroke="#8cc63f" stroke-width="2"/><path d="M20 12l6 12-3-1-2 4-2-1 2-4-3-1z" fill="#8cc63f"/></svg><h3>Virtual Receptionist</h3><p>Dunmerio agents answer calls just like an in-office receptionist – but for a fraction of the price.</p></div>
  <div class="feature" style="left:455px;top:150px"><svg width="40" height="36" viewBox="0 0 40 36"><rect x="4" y="8" width="32" height="22" fill="none" stroke="#8cc63f" stroke-width="2"/><path d="M4 8l16 12 16-12" fill="none" stroke="#8cc63f" stroke-width="2"/></svg><h3>Message Taking</h3><p>Use our agents as your personal assistant for general purpose message taking.</p></div>
  <div class="feature" style="left:800px;top:150px"><svg width="40" height="36" viewBox="0 0 40 36"><rect x="5" y="6" width="30" height="26" fill="none" stroke="#8cc63f" stroke-width="2"/><line x1="5" y1="13" x2="35" y2="13" stroke="#8cc63f" stroke-width="2"/><line x1="12" y1="2" x2="12" y2="9" stroke="#8cc63f" stroke-width="2"/><line x1="28" y1="2" x2="28" y2="9" stroke="#8cc63f" stroke-width="2"/></svg><h3>Appointment Scheduling</h3><p>24/7 agents book and manage appointments in your web-based calendaring service.</p></div>

  <div class="feature" style="left:110px;top:325px"><svg width="40" height="36" viewBox="0 0 40 36"><rect x="8" y="4" width="24" height="30" fill="none" stroke="#8cc63f" stroke-width="2"/><circle cx="20" cy="14" r="4" fill="#8cc63f"/><line x1="13" y1="24" x2="27" y2="24" stroke="#8cc63f" stroke-width="2"/></svg><h3>Lead Collection</h3><p>Never miss a lead again. Get accurate, 24/7 data entry from agents who are always available.</p></div>
  <div class="feature" style="left:800px;top:325px"><svg width="40" height="36" viewBox="0 0 40 36"><rect x="6" y="6" width="28" height="24" fill="none" stroke="#8cc63f" stroke-width="2"/><line x1="12" y1="14" x2="28" y2="14" stroke="#8cc63f" stroke-width="2"/><line x1="12" y1="21" x2="28" y2="21" stroke="#8cc63f" stroke-width="2"/></svg><h3>Event Registrations</h3><p>Putting on an event? Let our agents handle the overhead of attendee registrations and related calls.</p></div>

  <div class="feature" style="left:110px;top:485px"><svg width="40" height="36" viewBox="0 0 40 36"><rect x="5" y="8" width="30" height="20" rx="2" fill="none" stroke="#8cc63f" stroke-width="2"/><line x1="5" y1="14" x2="35" y2="14" stroke="#8cc63f" stroke-width="3"/></svg><h3>Order Processing</h3><p>Using our software or a portal you maintain, agents directly process sales for you.</p></div>
  <div class="feature" style="left:800px;top:505px"><svg width="40" height="36" viewBox="0 0 40 36"><circle cx="14" cy="11" r="6" fill="#8cc63f"/><circle cx="27" cy="14" r="5" fill="#8cc63f"/><path d="M3 32c0-9 22-9 22 0z" fill="#8cc63f"/><path d="M22 32c1-7 15-7 16 0z" fill="#8cc63f"/></svg><h3>Overflow Calls</h3><p>Automatically forward callers to our agents when you're tied up on the other line.</p></div>

  <div class="feature" style="left:110px;top:702px"><h3>After Hours/Lunch Coverage</h3><p>Callers should never get voicemail. Send them to a live person when you can't be there to answer.</p></div>
  <div class="feature" style="left:800px;top:723px"><h3>Call Transfers</h3><p>When callers need to speak with you, our system makes it easy for us to transfer the call to you.</p></div>

  <div class="phone-photo" role="img" aria-label="Photo of a hand holding a smartphone showing the app screen"></div>
  <div class="cta">Learn More About Our Answer Services</div>
</section>

<section class="languages">
  <div class="lang" style="left:120px"><h2>English</h2><h3>24/7 Coverage</h3><p>With Dunmerio's 24/7 answering service, you get a team of more than 125 virtual receptionists around the clock – even on holidays. And these aren't just any agents. We hire only the best and train our agents to provide a perfect blend of friendliness, professionalism, and business savvy, so that you can rest easy knowing that every single call is being answered quickly and handled correctly.</p></div>
  <div class="greeting-art" role="img" aria-label="Illustration of two speech bubbles greeting in English and Spanish"></div>
  <div class="lang" style="left:795px"><h2>Spanish</h2><h3>7am to Midnight</h3><p>Did you know that the US has over 41M residents that speak only Spanish, and another 12M residents that speak both English and Spanish? That's 1 in 6 US residents, making Spanish coverage a smart option for any business and a must-have for businesses that operate in markets like Florida, California, and other states with a high percentage of Spanish speaking residents. Add bilingual to any package for a flat fee of $20/mo.</p></div>
  <h2 class="rule-heading">Award-winning service on every call</h2>
</section>

<section class="testimonial">
  <div class="tabs-card">
    <div class="tab-row"><div class="tab current">Message Taking</div><div class="tab">Message Taking</div><div class="tab">Message Taking</div><div class="tab">Message Taking</div><div class="tab">Message Taking</div></div>
    <div class="client-photo" role="img" aria-label="Portrait of a customer"></div>
    <p class="tab-text">Make your customers feel heard by never sending them to voicemail. This customer needs help after hours. When Fairway Fitters cannot answer calls, the information is collected by a real person at Dunmerio and can be acted on first thing in the morning by a Fairway Fitters representative.</p>
  </div>
</section>

<section class="stats">
  <div class="stat" style="left:120px"><h3>Experienced</h3><div class="stat-body"><span class="stat-num">27</span><p>years as the trusted choice of thousands of businesses across dozens of industries.</p></div></div>
  <div class="stat" style="left:458px"><h3>Accomplished</h3><div class="stat-body"><span class="stat-num">3</span><p>years as the trusted choice of thousands of businesses across dozens of industries.</p></div></div>
  <div class="stat" style="left:795px"><h3>Consistent</h3><div class="stat-body"><span class="stat-num">24</span><p>years as the trusted choice of thousands of businesses across dozens of industries.</p></div></div>
</section>

<section class="demo">
  <h2>Request a demo and hear our agents in action</h2>
  <div class="field" style="top:197px">Name</div>
  <div class="field" style="top:267px">Email Address</div>
  <div class="field" style="top:342px">Phone</div>
  <div class="field message" style="top:422px">Message</div>
  <span class="captcha-label">4 + 2 =</span>
  <div class="captcha-box"></div>
  <div class="submit">Submit</div>
</section>

<footer class="site-footer">
  <div class="footer-art" role="img" aria-label="Connected service icons arranged around a central hub"></div>
  <ul class="footer-links" style="left:372px"><li>Services</li><li>Blog</li><li>FAQ</li></ul>
  <ul class="footer-links" style="left:625px"><li>Services</li><li>Blog</li><li>FAQ</li></ul>
  <ul class="footer-links" style="left:883px"><li>Services</li><li>Blog</li><li>FAQ</li></ul>
</footer>
<section class="footer-bar">
  <p class="legal">© dunmerio.com, Inc 2017. All rights reserved. <b>Privacy Policy</b> | <b>Terms of Service</b></p>
  <div class="social"><span></span><span></span><span></span><span></span></div>
</section>

</body>
</html>
```